Safety Brochure for Industry Assocations

This is an 8.5 x 11 single sided brochure for our Occupational Health and Safety Data Analytics software. If you need to use stock images we will pay for them.

Please incorporate our logo and some of the images. No need to incorporate them all. We like the idea of the boots being at the bottom of the page but we're open to other ideas.

Please note that we intend to mail this brochure to different industries so it should be generic (i.e. not construction specific).

Target Market(s)

Safety and Industry Organisations for construction, mining, forestry and oil and gas industries.

Industry/Entity Type

Industry

Font styles to use
Sans Serif

Colors

Designer to choose colors to be used in the design.

Requirements
Must have
• We are a software company that produces safety software. Our customers are companies that engage in dangerous work and use our software to improve their worker's safety. The look and feel should convey the fact that:
• -We are Big Data
• -We are Software
• -We service industry
Nice to have
• Please see the Pixlore photo of the boots. We were hoping that the desiger would be able ti modify the image with an overlay of 0's and 1's in a kind of "matrix" fashion to indicate that we are merging traditional labour work with software.
Should not have
• No medical symbols. Note that WE ARE NOT HEALTH CARE.

```html
<!DOCTYPE html>
<html lang="en">
<head>
<meta charset="utf-8">
<title>Safemetric Analytics – Injury Reduction Brochure</title>
<link href="https://fonts.googleapis.com/css2?family=Bebas+Neue&family=Roboto:ital,wght@0,400;0,700;0,900;1,400;1,700&family=Roboto+Condensed:ital,wght@0,400;0,700;1,700&display=swap" rel="stylesheet">
<style>
  :root {
    --green: #138c48;
    --green-light: #4cb64a;
    --lime: #9dcb3b;
    --charcoal: #474747;
    --bar-dark: #3d3d3d;
    --yellow: #f2ea4c;
    --white: #ffffff;
    --ink: #1d1d1d;
    --phone-green: #1b7a3c;
    --page-bg: #e6e6e6;
  }
  * { box-sizing: border-box; margin: 0; padding: 0; }
  html, body { width: 1200px; height: 1200px; overflow: hidden; }
  body { background: var(--page-bg); position: relative; font-family: "Roboto", Arial, sans-serif; }

  .brochure {
    position: absolute; left: 165px; top: 37px;
    width: 870px; height: 1126px;
    background: var(--white); overflow: hidden;
    box-shadow: 0 4px 18px rgba(0,0,0,.18);
  }
  .backdrop { position: absolute; inset: 0; width: 870px; height: 1126px; }

  .intro { position: absolute; left: 48px; top: 22px; color: var(--white); }
  .intro__lead { font-style: italic; font-size: 17px; }
  .intro__title { font-family: "Bebas Neue", sans-serif; font-size: 50px; line-height: 1; margin-top: 4px; }

  .benefits { position: absolute; left: 52px; top: 100px; list-style: none; color: var(--yellow);
    font-family: "Roboto", sans-serif; font-weight: 700; font-size: 14.5px; line-height: 1.3; }
  .benefits li { margin-bottom: 9px; }
  .benefits li:nth-child(2) { margin-left: 2px; }
  .benefits li:nth-child(3) { margin-left: 5px; }
  .benefits li:nth-child(4) { margin-left: 7px; }
  .benefits li:nth-child(5) { margin-left: 10px; }
  .benefits strong { font-weight: 900; }

  .brand { position: absolute; left: 448px; top: 84px; display: flex; align-items: center; gap: 10px; }
  .brand__dot { width: 56px; height: 56px; border-radius: 50%; background: var(--green-light); flex: none; }
  .brand__name { font-family: "Roboto", sans-serif; font-weight: 400; color: var(--charcoal);
    font-size: 20px; letter-spacing: 2px; line-height: 1.2; white-space: nowrap; }

  .service { position: absolute; right: 120px; text-align: right; color: var(--white);
    font-family: "Roboto Condensed", sans-serif; font-size: 15.5px; line-height: 1.5; }
  .service__title { font-family: "Roboto Condensed", sans-serif; font-style: italic; font-weight: 700;
    color: var(--lime); font-size: 36px; line-height: 1.15; margin-bottom: 6px; }
  .service--training { top: 226px; }
  .service--benchmark { top: 370px; right: 105px; }
  .service--trend { top: 530px; right: 100px; }

  .headline { position: absolute; left: 76px; top: 452px; color: var(--ink); }
  .headline__lead { font-weight: 700; font-size: 40px; line-height: 1; }
  .headline__big { font-family: "Bebas Neue", sans-serif; color: var(--lime); font-size: 122px; line-height: .8; margin-top: 10px; }
  .headline__sub { font-weight: 700; font-size: 31px; line-height: 1.1; margin-top: 0; }
  .headline__note { font-size: 17px; letter-spacing: 1px; color: #333; margin-top: 2px; }

  .boots-photo { position: absolute; left: 318px; top: 684px; width: 470px; height: 290px;
    border-radius: 40% 40% 18% 18% / 30% 30% 14% 14%;
    background: radial-gradient(ellipse at 40% 45%, #7a5a3a 0%, #5a3f28 45%, #3a2a1c 80%, #2b241f 100%); }

  .screen { position: absolute; left: 98px; top: 813px; width: 285px; height: 190px;
    background: #111; border-radius: 6px; padding: 9px; }
  .screen__display { width: 100%; height: 100%;
    background: linear-gradient(180deg, #dfe7f2 0%, #f4f6f9 30%, #f7e4e4 60%, #eef2f7 100%); }
  .screen__stand { position: absolute; left: 210px; top: 1003px; width: 60px; height: 22px;
    background: linear-gradient(180deg, #bdbdbd, #e8e8e8); clip-path: polygon(20% 0, 80% 0, 100% 100%, 0 100%); }

  .contact { position: absolute; left: 320px; top: 1040px; width: 520px; text-align: center; }
  .contact__web { font-family: "Roboto", sans-serif; font-size: 26px; letter-spacing: 6px; color: var(--ink); white-space: nowrap; }
  .contact__phone { font-family: "Roboto Condensed", sans-serif; font-weight: 700; font-size: 33px; color: var(--phone-green); margin-top: 2px; }
</style>
</head>
<body>
<main class="brochure">
  <svg class="backdrop" viewBox="0 0 870 1126" aria-hidden="true">
    <rect class="band-top" x="0" y="0" width="870" height="400" fill="var(--green)"/>
    <polygon class="band-side" points="745,0 870,0 870,975 400,1080 400,380" fill="var(--charcoal)"/>
    <rect class="panel-light" x="0" y="290" width="150" height="200" fill="var(--green-light)"/>
    <path class="arc-green" d="M150 282 A358 358 0 0 1 508 640 L150 640 Z" fill="var(--green)"/>
    <line class="arc-divider" x1="154" y1="282" x2="154" y2="395" stroke="#9a9a9a" stroke-width="6"/>
    <circle class="arc-white" cx="215" cy="780" r="365" fill="var(--white)"/>
    <rect x="400" y="640" width="470" height="440" fill="var(--charcoal)"/>
    <polygon points="400,1080 870,975 870,1126 400,1126" fill="var(--white)"/>
    <path class="arc-lime" d="M0 830 Q40 1020 200 1080 L200 1126 L0 1126 Z" fill="var(--lime)"/>

    <g class="bar-chart" fill="var(--bar-dark)">
      <rect x="73" y="713" width="58" height="180"/>
      <rect x="137" y="663" width="59" height="230"/>
      <rect x="213" y="758" width="59" height="135"/>
    </g>

    <g class="cloud cloud--logo" fill="var(--white)" style="filter:drop-shadow(0 0 1.5px #9a9a9a)">
      <ellipse cx="550" cy="120" rx="170" ry="70"/>
      <circle cx="470" cy="70" r="50"/><circle cx="560" cy="45" r="45"/>
      <circle cx="640" cy="60" r="48"/><circle cx="690" cy="120" r="42"/>
      <circle cx="410" cy="120" r="40"/><circle cx="460" cy="170" r="40"/>
      <circle cx="560" cy="180" r="35"/><circle cx="650" cy="170" r="40"/>
    </g>

    <g class="cloud cloud--bars" fill="var(--white)" style="filter:drop-shadow(0 0 1.5px #9a9a9a)">
      <ellipse cx="460" cy="290" rx="85" ry="38"/>
      <circle cx="420" cy="268" r="25"/><circle cx="470" cy="258" r="28"/><circle cx="515" cy="275" r="25"/>
      <circle cx="400" cy="305" r="20"/><circle cx="455" cy="320" r="22"/><circle cx="510" cy="310" r="20"/>
    </g>
    <g class="mini-bars">
      <rect x="412" y="290" width="5" height="14" fill="#e04545"/><rect x="418" y="282" width="5" height="22" fill="#8a44b8"/>
      <rect x="428" y="278" width="5" height="26" fill="#f3c133"/><rect x="434" y="286" width="5" height="18" fill="#e04545"/>
      <rect x="444" y="292" width="5" height="12" fill="#4aa8d8"/><rect x="450" y="280" width="5" height="24" fill="#8a44b8"/>
      <rect x="460" y="288" width="5" height="16" fill="#e04545"/><rect x="466" y="294" width="5" height="10" fill="#6cc04a"/>
      <rect x="476" y="286" width="5" height="18" fill="#f3c133"/><rect x="482" y="290" width="5" height="14" fill="#e04545"/>
      <rect x="492" y="292" width="5" height="12" fill="#8a44b8"/><rect x="498" y="288" width="5" height="16" fill="#e04545"/>
      <line x1="408" y1="304" x2="506" y2="304" stroke="#999" stroke-width="1"/>
    </g>

    <g class="cloud cloud--network" fill="var(--white)" style="filter:drop-shadow(0 0 1.5px #9a9a9a)">
      <ellipse cx="450" cy="413" rx="72" ry="36"/>
      <circle cx="415" cy="392" r="24"/><circle cx="460" cy="384" r="26"/><circle cx="500" cy="402" r="22"/>
      <circle cx="400" cy="428" r="20"/><circle cx="450" cy="440" r="20"/><circle cx="496" cy="430" r="18"/>
    </g>
    <g class="mini-network" stroke="#e07a3a" stroke-width="1" fill="none">
      <polygon points="450,392 474,402 480,426 452,440 424,428 420,404"/>
      <polygon points="450,404 466,410 468,424 452,430 436,424 434,410"/>
      <line x1="450" y1="392" x2="452" y2="440"/><line x1="420" y1="404" x2="480" y2="426"/><line x1="474" y1="402" x2="424" y2="428"/>
    </g>

    <g class="cloud cloud--small" fill="var(--white)" style="filter:drop-shadow(0 0 1.5px #9a9a9a)">
      <ellipse cx="494" cy="515" rx="44" ry="20"/>
      <circle cx="478" cy="503" r="15"/><circle cx="505" cy="500" r="16"/><circle cx="525" cy="512" r="13"/>
    </g>
    <g class="cloud cloud--tiny" fill="var(--white)" style="filter:drop-shadow(0 0 1.5px #9a9a9a)">
      <ellipse cx="474" cy="587" rx="23" ry="11"/>
      <circle cx="466" cy="580" r="9"/><circle cx="482" cy="579" r="9"/>
    </g>
  </svg>

  <header class="intro">
    <p class="intro__lead">Leverage the power of</p>
    <h1 class="intro__title">BIG DATA!</h1>
  </header>

  <ul class="benefits">
    <li><strong>LEAD</strong> the next wave of injury reduction</li>
    <li><strong>ENGAGE</strong> with members through collaboration<br>and benchmarking</li>
    <li><strong>PROMOTE</strong> standardization</li>
    <li><strong>ANALYZE</strong> Accurate, Timely and Complete<br>Leading Indicators</li>
    <li><strong>TRAIN</strong> industry more proactively</li>
  </ul>

  <div class="brand">
    <span class="brand__dot"></span>
    <span class="brand__name">SAFEMETRIC<br>Analytics</span>
  </div>

  <section class="service service--training">
    <h2 class="service__title">Training</h2>
    <p>Analyze needs of Industry<br>Deliver Proactive Training<br>Improve Safety</p>
  </section>
  <section class="service service--benchmark">
    <h2 class="service__title">Benchmarking</h2>
    <p>Engage with Members<br>Promote Collaborative Advancement<br>of Safety<br>Improve Safety</p>
  </section>
  <section class="service service--trend">
    <h2 class="service__title">Trend Analysis</h2>
    <p>Monitor Industry Trends<br>Implement Corrective Initiatives<br>Improve Safety</p>
  </section>

  <div class="headline">
    <p class="headline__lead">The next</p>
    <p class="headline__big">BIG STEP</p>
    <p class="headline__sub">in injury reduction!</p>
    <p class="headline__note">For your entire industry</p>
  </div>

  <div class="boots-photo" role="img" aria-label="Photo of a pair of worn leather work boots"></div>

  <div class="screen">
    <div class="screen__display" role="img" aria-label="Screenshot of the safety analytics dashboard with charts and tables"></div>
  </div>
  <div class="screen__stand"></div>

  <footer class="contact">
    <p class="contact__web">www.safemetricdata.com</p>
    <p class="contact__phone">1-888-555-0142</p>
  </footer>
</main>
</body>
</html>
```